Halt and Thicken New Branding Stationary Set - updated Oct 30th 2017

Updated on 30th Oct 2017 as we now need a whole folder design instead of a folder cover. We have thought out exactly what should be on it so it wont be hard. We are happy for this to be completed only by the winning designer if you like. And also we are guaranteeing this project now. Thanks!

We just got our new logo and now we would like a stationary set so we can brand our company communications. The items we need designed are:
Business cards
Letterhead
Appointment confirmation cards
Folder - switched from folder cover. Note that if you don't wish to do this unless you are selected as the winner this is fine.

1. Business cards - for 5 employees, final names will be given once the winner is selected, but you can use this one as the sample:
Lucinda Marquez
Hair Regrowth Expert
Halt and Thicken
7182 Oakmere Ave, Suite 500
Beverly Hills CA 90299
lucinda@jamesholloway-md.example
(310) 555-0193

2. Letterhead 8.5" x 11.0" vertical
Halt and Thicken
Beverly Hills CA 90299
office@haltandthicken.example
(310) 555-0193

3. Appointment Confirmation cards - business card size
Halt and Thicken
Beverly Hills CA 90299
Appointment For:
Date:
Time:
If you are unable to make your appointment, please contact us to reschedule at:
(310) 555-0193
info@jamesholloway-md.example

*UPDATED*
4. Folder 9" x 12 " vertical with double pocket
We would like the infinity image from the logo made really big so the left side is on the back and the right side with the + sign is on the front and its takes up the maximum room on the folder.
On the front below the half logo it should say "A Biochemical Revolution..."
On the inside we would also like to have the infinity sign from the logo but faded and half on the left pocket half on the right.
On left inside pocket it should say (this will be partically written on top of the logo):
James Holloway MD
Precision Medicine
Halt and Thicken Hair
On the Right inside pocket it should say the following:
Because the Enemy of BETTER Health is Good Health
BETTER Ingredients
BETTER Recipe
BETTER Medicine
On the back below the logo on the bottom should be the contact information.
I attached a picture of our drawing of what we want for this to make it easier.

Here is our website to give you an idea of our branding: http://www.haltandthicken.example/

We are the only true cure for hair loss and need to look professional and highest quality and beyond reproach from an ethical standpoint. We are a medical clinic so this should be portrayed also.
We cured hair loss by analyzing biochemistry and rebalancing it so that the process reverses and your own hair can grow back naturally.

Business card information:

OK so here is the information for the business cards:

Lucinda Marquez
Hair Regrowth Expert
(310) 555-0193
www.haltandthicken.example

Marisol Quintero
Hair Growth Consultant
(310) 555-0193
marisol@jamesholloway-md.example
www.haltandthicken.example

Janice Pelham
CMO/COO
(310) 555-0193
janice@haltandthicken.example
www.haltandthicken.example

Dr Glen Holloway
President
(310) 555-0193
info@jamesholloway-md.example
www.haltandthicken.example

Halt and Thicken
Customer Service
(310) 555-0193
info@jamesholloway-md.example
www.haltandthicken.example

Target Market(s)

Men aged 20-24 who care about their appearance, care about their hair and care about the world.

Industry/Entity Type

Medical And Science

Font styles to use
Sans Serif

Colors
00a990
ffffff
9d9d9d
333333

Requirements
Must have
• Must use the logo and our brand colors from the logo in all designs.
• The pantone colors are:
• Green: #4ca26f
• Light Grey: #999999
• The design should be symmetrical and balanced.
Nice to have
• It should look reasonably masculine.
Should not have
• Do not include any red in the design.

```html
<!DOCTYPE html>
<html lang="en">
<head>
<meta charset="utf-8">
<title>Halt and Thicken – Appointment Card</title>
<link href="https://fonts.googleapis.com/css2?family=Roboto+Condensed:wght@700&family=Open+Sans:wght@400&display=swap" rel="stylesheet">
<style>
  :root {
    --stage: #0e0b26;
    --card-white: #ffffff;
    --brand-green: #48d84a;
    --text-green: #45cf46;
    --ink: #3a3b46;
    --on-green: #ffffff;
  }
  html, body {
    margin: 0;
    padding: 0;
    overflow: hidden;
  }
  .stage {
    position: relative;
    width: 1171px;
    height: 1200px;
    background: var(--stage);
    overflow: hidden;
    font-family: "Roboto Condensed", "Arial Narrow", sans-serif;
    font-weight: 700;
  }
  .card {
    position: absolute;
    left: 235px;
    width: 699px;
    height: 399px;
    box-sizing: border-box;
  }
  .card--front {
    top: 163px;
    background: var(--card-white);
    color: var(--ink);
  }
  .card--back {
    top: 638px;
    background: var(--brand-green);
    color: var(--on-green);
  }
  .clinic-name {
    position: absolute;
    left: 58px;
    top: 57px;
    margin: 0;
    font-size: 22px;
    color: var(--text-green);
    line-height: 1;
  }
  .address {
    position: absolute;
    left: 58px;
    top: 84px;
    margin: 0;
    font-style: normal;
    font-size: 22px;
    line-height: 28px;
  }
  .appointment-heading {
    position: absolute;
    left: 58px;
    top: 158px;
    margin: 0;
    font-size: 22px;
    color: var(--text-green);
    line-height: 1;
  }
  .appointment-field {
    position: absolute;
    left: 62px;
    margin: 0;
    font-size: 22px;
    line-height: 1;
    display: flex;
    align-items: baseline;
  }
  .appointment-field--date { top: 203px; }
  .appointment-field--time { top: 242px; }
  .field-label {
    display: inline-block;
    width: 78px;
  }
  .field-line {
    display: inline-block;
    width: 215px;
    border-bottom: 2px dotted var(--ink);
    transform: translateY(-2px);
  }
  .reschedule {
    position: absolute;
    left: 0;
    right: 0;
    top: 296px;
    margin: 0;
    text-align: center;
    font-size: 16.5px;
    color: var(--text-green);
    line-height: 1;
  }
  .contact-phone {
    position: absolute;
    left: 0;
    right: 0;
    top: 327px;
    margin: 0;
    text-align: center;
    font-size: 24px;
    line-height: 1;
  }
  .contact-email {
    position: absolute;
    left: 0;
    right: 0;
    top: 356px;
    margin: 0;
    text-align: center;
    font-size: 16px;
    line-height: 1;
  }
  .brand-lockup {
    position: absolute;
    display: flex;
    align-items: center;
    gap: 10px;
    line-height: 1;
  }
  .brand-lockup--front {
    left: 452px;
    top: 86px;
    color: var(--text-green);
    font-size: 25px;
  }
  .brand-lockup--back {
    left: 0;
    right: 0;
    top: 160px;
    justify-content: center;
    color: var(--on-green);
    font-size: 40px;
  }
  .brand-dot {
    display: block;
    flex: none;
  }
  .website {
    position: absolute;
    left: 0;
    right: 0;
    top: 232px;
    margin: 0;
    text-align: center;
    font-family: "Open Sans", Arial, sans-serif;
    font-weight: 400;
    font-size: 23px;
    letter-spacing: 0.3px;
    line-height: 1;
  }
</style>
</head>
<body>
<main class="stage">
  <section class="card card--front" aria-label="Appointment card, front">
    <h1 class="clinic-name">Halt and Thicken</h1>
    <address class="address">7182 Oakmere Ave, Suite 500<br>Beverly Hills CA 90299</address>

    <div class="brand-lockup brand-lockup--front">
      <svg class="brand-dot" width="22" height="22" viewBox="0 0 22 22" aria-hidden="true">
        <circle cx="11" cy="11" r="11" fill="var(--text-green)"/>
      </svg>
      <span>Halt and Thicken</span>
    </div>

    <h2 class="appointment-heading">Appointment For:</h2>
    <p class="appointment-field appointment-field--date">
      <span class="field-label">Date&nbsp; :-</span><span class="field-line"></span>
    </p>
    <p class="appointment-field appointment-field--time">
      <span class="field-label">Time&nbsp; :-</span><span class="field-line"></span>
    </p>

    <p class="reschedule">If you are unable to make your appointment, please contact us to reschedule at:</p>
    <p class="contact-phone">(310) 555-0193</p>
    <p class="contact-email">info@jamesholloway-md.example</p>
  </section>

  <section class="card card--back" aria-label="Appointment card, back">
    <div class="brand-lockup brand-lockup--back">
      <svg class="brand-dot" width="30" height="30" viewBox="0 0 30 30" aria-hidden="true">
        <circle cx="15" cy="15" r="15" fill="var(--on-green)"/>
      </svg>
      <span>Halt and Thicken</span>
    </div>
    <p class="website">www.haltandthicken.example</p>
  </section>
</main>
</body>
</html>
```